Business Card Design

Im a small business that specialises in all aspects of sign installation, big and small, domestic and commercial. I have a construction and carpentry background. I'm after a professional looking business card, that has my logo as the forefront of the card incorporating the same colours as the my logo. No slogan as yet, but open to suggestions. The final design should communicate quality and class workmanship.

Target Market(s)

Managers and Owners of businesses

Industry/Entity Type

Small Business

Contact Information for Business Card

Carwyn Solbeck
Mob: 0417295036
Email: kto.fitouts@quillmail.net

Sign Installation
Property Improvement and Maintenance
Trade Services

Colors
dbdbdb
000000
ffffff

Requirements
Must have
• Logo
My name
My contact details
What I specialise in
Nice to have
• background image/images that are only just noticeable and do not take away from the logo or text.
Should not have
• No colours that contrast from my logo
No heavy machinery images to be used
Logo must stand out

```html
<!DOCTYPE html>
<html lang="en">
<head>
<meta charset="utf-8">
<title>KTO Fitouts – Business Card</title>
<link rel="stylesheet" href="https://fonts.googleapis.com/css2?family=Mulish:wght@400;700;800&display=swap">
<style>
  :root {
    --backdrop: #2b2b2d;
    --card-white: #ffffff;
    --card-grey: #e6e6e8;
    --brand-blue: #0b4a9e;
    --brand-blue-deep: #083c82;
    --ink: #1a1a1a;
    --faint: #dcdcde;
  }
  * { box-sizing: border-box; margin: 0; padding: 0; }
  html, body {
    width: 1200px; height: 900px; overflow: hidden;
    background: var(--backdrop);
    font-family: "Mulish", "Century Gothic", sans-serif;
  }
  .canvas {
    width: 1200px; height: 900px;
    display: flex; flex-direction: column;
    align-items: center; justify-content: center; gap: 40px;
  }
  .card {
    position: relative;
    width: 700px; height: 400px;
    background: radial-gradient(ellipse at 40% 40%, var(--card-white) 0%, var(--card-white) 45%, var(--card-grey) 100%);
    box-shadow: 0 14px 30px rgba(0,0,0,0.45);
    overflow: hidden;
  }
  .card__band {
    position: absolute; left: 0; right: 0; bottom: 0;
    height: 34px;
    background: var(--brand-blue);
    display: flex; align-items: center; justify-content: center;
    color: var(--card-white);
    font-size: 13px; font-weight: 700;
    letter-spacing: 1.2px; text-transform: uppercase;
    white-space: nowrap;
  }
  .card__band .sep { margin: 0 10px; opacity: 0.7; }
  .brand {
    display: flex; align-items: center; gap: 18px;
    white-space: nowrap;
    z-index: 1;
  }
  .brand__circle {
    width: 80px; height: 80px; border-radius: 50%;
    border: 7px solid var(--brand-blue);
    flex: none;
  }
  .brand__name {
    color: var(--brand-blue);
    font-weight: 800;
    font-size: 52px;
    letter-spacing: 1px;
    text-transform: uppercase;
    line-height: 1;
  }
  /* Front */
  .card--front .brand {
    position: absolute; left: 50%; top: 175px;
    transform: translate(-50%, -50%);
  }
  /* Back */
  .card--back .brand {
    position: absolute; left: 42px; top: 40px;
  }
  .card--back .brand__circle { width: 66px; height: 66px; border-width: 6px; }
  .card--back .brand__name { font-size: 40px; }
  .card__watermark {
    position: absolute; right: -20px; top: 60px;
    width: 240px; height: 240px; border-radius: 50%;
    border: 18px solid var(--faint);
    opacity: 0.8;
    z-index: 0;
  }
  .contact {
    position: absolute; left: 48px; top: 190px;
    z-index: 1;
  }
  .contact__name {
    color: var(--brand-blue);
    font-weight: 700;
    font-size: 24px;
    margin-bottom: 20px;
  }
  .contact__row {
    display: flex; align-items: center; gap: 16px;
    font-size: 20px; color: var(--ink);
    margin-bottom: 14px;
    letter-spacing: 0.5px;
  }
  .contact__icon { width: 20px; height: 20px; flex: none; fill: var(--brand-blue-deep); }
</style>
</head>
<body>
<main class="canvas">
  <section class="card card--front" aria-label="Card front">
    <div class="brand">
      <span class="brand__circle" aria-hidden="true"></span>
      <span class="brand__name">KTO Fitouts</span>
    </div>
    <p class="card__band">Sign Installation<span class="sep">•</span>Property Improvement and Maintenance<span class="sep">•</span>Trade Services</p>
  </section>

  <section class="card card--back" aria-label="Card back">
    <div class="card__watermark" aria-hidden="true"></div>
    <div class="brand">
      <span class="brand__circle" aria-hidden="true"></span>
      <span class="brand__name">KTO Fitouts</span>
    </div>
    <div class="contact">
      <p class="contact__name">Carwyn Solbeck</p>
      <p class="contact__row">
        <svg class="contact__icon" viewBox="0 0 20 20" aria-hidden="true">
          <rect x="5" y="1" width="10" height="18" rx="2"/>
          <rect x="7" y="4" width="6" height="6" fill="#fff"/>
          <circle cx="10" cy="15" r="1.4" fill="#fff"/>
        </svg>
        <span>0417295036</span>
      </p>
      <p class="contact__row">
        <svg class="contact__icon" viewBox="0 0 20 20" aria-hidden="true">
          <rect x="1" y="4" width="18" height="12" rx="1.5"/>
          <path d="M2 5 L10 11 L18 5" stroke="#fff" stroke-width="1.6" fill="none"/>
        </svg>
        <span>kto.fitouts@quillmail.net</span>
      </p>
    </div>
    <p class="card__band">Sign Installation<span class="sep">•</span>Property Improvement and Maintenance<span class="sep">•</span>Trade Services</p>
  </section>
</main>
</body>
</html>
```